TBV business card

For a business card with our logo

Contact Information for Business Card

Lucien MARVET
Founder & CEO
email : ceo@brightlanternstudio.com / www.brightlanternstudio.com /
instagram / facebook / WhatsApp
N°: +590 690 482 517

Colors

Designer to choose colors to be used in the design.

```html
<!DOCTYPE html>
<html lang="en">
<head>
<meta charset="utf-8">
<title>TBV Studio – Business Card</title>
<link rel="stylesheet" href="https://fonts.googleapis.com/css2?family=Tinos:wght@400&family=Questrial&display=swap">
<style>
  :root {
    --orange: #f37329;
    --blue: #1556a5;
    --ink: #4f4f52;
    --rule: #a7a7a9;
    --paper: #ffffff;
    --back: #07080a;
    --stage: #f3f3f5;
  }
  * { margin: 0; padding: 0; box-sizing: border-box; }
  html, body { width: 1200px; height: 1200px; overflow: hidden; background: var(--stage); }
  .canvas { position: relative; width: 1200px; height: 1200px; }

  .card { position: absolute; left: 206px; width: 788px; height: 450px; overflow: hidden; }
  .card-front { top: 112px; background: var(--paper); }
  .card-back { top: 635px; background: var(--back); }

  .brand { position: absolute; left: 56px; top: 58px; width: 270px; text-align: center; }
  .brand-mark { display: block; margin: 0 auto 8px; width: 108px; height: 108px; border-radius: 50%; background: var(--orange); }
  .brand-name { font-family: "Tinos", serif; font-size: 34px; color: var(--blue); letter-spacing: 0.5px; line-height: 1; }

  .person { position: absolute; right: 77px; top: 114px; text-align: right; }
  .person-name { font-family: "Tinos", serif; font-size: 29px; color: var(--blue); letter-spacing: 0.3px; line-height: 1; }
  .person-role { font-family: "Tinos", serif; font-size: 15px; line-height: 1; color: var(--ink); margin-top: 7px; margin-right: 12px; }

  .contact { position: absolute; display: flex; align-items: center; gap: 10px;
             font-family: "Questrial", sans-serif; color: var(--ink); }
  .contact-phone { left: 54px; top: 287px; font-size: 21px; letter-spacing: 0.6px; }
  .contact-mail { left: 54px; top: 361px; font-size: 19.5px; }
  .contact-web { left: 397px; top: 361px; font-size: 19.5px; gap: 20px; }
  .contact-icon { width: 27px; height: 27px; flex: none; }

  .socials { position: absolute; left: 574px; top: 278px; display: flex; gap: 14px; list-style: none; }
  .social-dot { width: 43px; height: 43px; border-radius: 50%; background: var(--blue); }

  .rule { position: absolute; left: 60px; top: 341px; width: 667px; height: 1.5px; background: var(--rule); }

  .band { position: absolute; bottom: 0; height: 12px; width: 50%; }
  .band-orange { left: 0; background: var(--orange); }
  .band-blue { right: 0; background: var(--blue); }

  .back-brand { position: absolute; inset: 0; display: flex; align-items: center; justify-content: center; gap: 26px; }
  .back-mark { width: 64px; height: 64px; border-radius: 50%; background: var(--orange); }
  .back-name { font-family: "Tinos", serif; font-size: 64px; color: var(--orange); letter-spacing: 1px; }
</style>
</head>
<body>
<main class="canvas">

  <section class="card card-front" aria-label="Business card front">
    <div class="brand">
      <span class="brand-mark" aria-hidden="true"></span>
      <div class="brand-name">TBV STUDIO</div>
    </div>

    <div class="person">
      <div class="person-name">LUCIEN MARVET</div>
      <div class="person-role">FOUNDER &amp; CEO</div>
    </div>

    <div class="contact contact-phone">
      <svg class="contact-icon" viewBox="0 0 28 28" aria-hidden="true">
        <circle cx="14" cy="14" r="14" fill="var(--orange)"/>
        <rect x="9.5" y="6" width="9" height="16" rx="1.8" fill="none" stroke="#fff" stroke-width="2"/>
        <circle cx="14" cy="18.6" r="1.1" fill="#fff"/>
      </svg>
      <span>+590 690 482 517</span>
    </div>

    <ul class="socials" aria-label="Social channels">
      <li class="social-dot" aria-label="Photo profile"></li>
      <li class="social-dot" aria-label="Community page"></li>
      <li class="social-dot" aria-label="Messaging"></li>
    </ul>

    <div class="rule"></div>

    <div class="contact contact-mail">
      <svg class="contact-icon" viewBox="0 0 28 28" aria-hidden="true">
        <circle cx="14" cy="14" r="14" fill="var(--orange)"/>
        <rect x="6.5" y="9" width="15" height="10.5" rx="1" fill="none" stroke="#fff" stroke-width="1.8"/>
        <path d="M6.8 9.5 L14 15 L21.2 9.5" fill="none" stroke="#fff" stroke-width="1.8"/>
      </svg>
      <span>ceo@brightlanternstudio.com</span>
    </div>

    <div class="contact contact-web">
      <svg class="contact-icon" viewBox="0 0 28 28" aria-hidden="true">
        <circle cx="14" cy="14" r="12.5" fill="none" stroke="var(--orange)" stroke-width="2.4"/>
        <circle cx="14" cy="14" r="7" fill="none" stroke="var(--orange)" stroke-width="1.8"/>
        <path d="M7 14 H21 M14 7 V21" stroke="var(--orange)" stroke-width="1.6"/>
      </svg>
      <span>www.brightlanternstudio.com</span>
    </div>

    <div class="band band-orange"></div>
    <div class="band band-blue"></div>
  </section>

  <section class="card card-back" aria-label="Business card back">
    <div class="back-brand">
      <span class="back-mark" aria-hidden="true"></span>
      <span class="back-name">TBV STUDIO</span>
    </div>
  </section>

</main>
</body>
</html>
```